Bref créative
Business card/letterhead/envelopes/fax cover sheet for plastic surgery practice
Morvan Plastic Surgery
Professional
Darek Olund, M.D.
unknown at this time
morvanaestheticclinic@mailbeam.example
www.darekolundmd.example
I would like name, address, phone number, fax number, and website included on front (no email address). I would also like the Continental Guild of Cosmetic Practice logo and Board Certified logo to appear on the front. The words "Plastic and Reconstructive Surgery, Hand Surgery, Cosmetic Surgery" should appear near or under my name.
The tagline "Results nobody can resist" should be included (front or back). Also, an area to write in the next appointment information should be on the back.
Continental Guild of Cosmetic Practitioners Logo
logo
Board Certification logo

```html
<!DOCTYPE html>
<html lang="en">
<head>
<meta charset="utf-8">
<title>Morvan Plastic Surgery – Business Card</title>
<link href="https://fonts.googleapis.com/css2?family=Open+Sans:wght@400;600;700&family=Merriweather:wght@700&display=swap" rel="stylesheet">
<style>
  :root {
    --navy: #1b2f8f;
    --royal: #2746c8;
    --sky: #3a7de0;
    --steel: #9aa3b4;
    --ink: #2b2f3a;
    --paper: #ffffff;
    --backdrop: #e9ebef;
    --badge-orange: #f29a1e;
    --badge-grey: #c9ced8;
  }
  * { box-sizing: border-box; margin: 0; padding: 0; }
  html, body { width: 1200px; height: 646px; overflow: hidden; }
  body {
    background: var(--backdrop);
    font-family: "Open Sans", Arial, sans-serif;
    color: var(--ink);
    position: relative;
  }
  .card {
    position: absolute;
    top: 173px;
    width: 525px;
    height: 300px;
    background: var(--paper);
    box-shadow: 0 6px 18px rgba(20, 30, 60, .18);
    overflow: hidden;
  }
  .card--back { left: 45px; }
  .card--front { left: 630px; }
  .card svg.card__art { position: absolute; inset: 0; }

  /* back side */
  .appointment__title {
    position: absolute; top: 26px; left: 0; right: 0;
    text-align: center;
    font-family: "Merriweather", Georgia, serif;
    font-size: 19px; color: var(--navy);
  }
  .appointment__field {
    position: absolute; left: 42px; right: 42px;
    display: flex; align-items: flex-end; gap: 10px;
    font-family: "Merriweather", Georgia, serif;
    font-size: 17px; color: var(--navy);
  }
  .appointment__field span.line {
    flex: 1; border-bottom: 1.5px dotted var(--steel); height: 18px;
  }
  .appointment__note {
    position: absolute; left: 42px; right: 42px; bottom: 26px;
    font-size: 11px; line-height: 1.5; color: var(--ink);
  }

  /* front side */
  .brand {
    position: absolute; top: 32px; left: 0; right: 0;
    text-align: center;
  }
  .brand__name {
    display: inline-flex; align-items: center; gap: 9px;
    font-size: 28px; font-weight: 600; color: var(--navy);
    letter-spacing: 3px; line-height: 1.1;
  }
  .brand__dot { width: 11px; height: 11px; border-radius: 50%; background: var(--sky); }
  .brand__sub {
    font-size: 11px; font-weight: 600; color: var(--navy);
    letter-spacing: 3px; margin-top: 4px;
  }
  .brand__tagline { font-size: 9px; font-style: italic; color: var(--steel); margin-top: 3px; }
  .badges { position: absolute; top: 20px; right: 22px; display: flex; gap: 10px; }
  .badge { width: 34px; height: 34px; border-radius: 50%; }
  .badge--guild { background: var(--badge-orange); }
  .badge--board { background: var(--badge-grey); }
  .doctor { position: absolute; top: 122px; left: 0; right: 0; text-align: center; }
  .doctor__name { font-size: 19px; font-weight: 700; color: var(--navy); }
  .doctor__specialties { font-size: 9.5px; color: var(--ink); margin-top: 2px; }
  .contact {
    position: absolute; bottom: 18px; left: 34px; right: 34px;
    display: flex; justify-content: space-between;
    color: var(--paper); font-size: 10.5px; line-height: 1.75;
  }
  .contact__item { display: flex; align-items: center; gap: 7px; }
  .contact__item svg { width: 11px; height: 11px; flex: none; }
</style>
</head>
<body>

<section class="card card--back" aria-label="Card back: next appointment">
  <svg class="card__art" viewBox="0 0 525 300" aria-hidden="true">
    <path d="M0 300 L0 190 C120 230 230 290 330 300 Z" fill="#eef1f6"/>
    <path d="M0 210 C110 245 210 290 300 300" fill="none" stroke="#d6dbe6" stroke-width="3"/>
  </svg>
  <h2 class="appointment__title">Next Appointment</h2>
  <div class="appointment__field" style="top:82px">For :<span class="line"></span></div>
  <div class="appointment__field" style="top:126px">Date :<span class="line"></span></div>
  <div class="appointment__field" style="top:170px">Time :<span class="line"></span></div>
  <p class="appointment__note">If you are unable to keep your appointment,<br>please call the office 24 hours in advance.</p>
</section>

<section class="card card--front" aria-label="Card front">
  <svg class="card__art" viewBox="0 0 525 300" aria-hidden="true">
    <defs>
      <linearGradient id="band" x1="0" y1="0" x2="1" y2="1">
        <stop offset="0" stop-color="#2746c8"/>
        <stop offset="1" stop-color="#1b2f8f"/>
      </linearGradient>
    </defs>
    <path d="M0 188 C170 226 340 210 525 160 L525 300 L0 300 Z" fill="#c7ccd8"/>
    <path d="M0 200 C170 238 340 222 525 172 L525 300 L0 300 Z" fill="url(#band)"/>
  </svg>

  <div class="badges">
    <span class="badge badge--guild" role="img" aria-label="Continental Guild of Cosmetic Practitioners badge"></span>
    <span class="badge badge--board" role="img" aria-label="Board certification badge"></span>
  </div>

  <div class="brand">
    <div class="brand__name"><span class="brand__dot"></span>MORVAN</div>
    <div class="brand__sub">PLASTIC SURGERY</div>
    <div class="brand__tagline">Results nobody can resist</div>
  </div>

  <div class="doctor">
    <div class="doctor__name">Darek Olund, M.D.</div>
    <div class="doctor__specialties">Plastic &amp; Reconstructive Surgery, Hand Surgery, Cosmetic Surgery</div>
  </div>

  <div class="contact">
    <div>
      <div class="contact__item">
        <svg viewBox="0 0 12 12"><path d="M2.5 1 L4.5 1 L5.3 3.5 L4 4.5 C4.6 5.9 6.1 7.4 7.5 8 L8.5 6.7 L11 7.5 L11 9.5 C11 10.3 10.3 11 9.5 11 C5 11 1 7 1 2.5 C1 1.7 1.7 1 2.5 1 Z" fill="#fff"/></svg>
        555 010 2468
      </div>
      <div class="contact__item">
        <svg viewBox="0 0 12 12"><path d="M6 0.5 C3.8 0.5 2.2 2.1 2.2 4.2 C2.2 7 6 11.5 6 11.5 C6 11.5 9.8 7 9.8 4.2 C9.8 2.1 8.2 0.5 6 0.5 Z" fill="#fff"/><circle cx="6" cy="4.2" r="1.4" fill="#2746c8"/></svg>
        Suite 410 Harrow Lane
      </div>
      <div class="contact__item" style="padding-left:18px">Elmshire, 40912 Norland</div>
    </div>
    <div>
      <div class="contact__item">
        <svg viewBox="0 0 12 12"><rect x="1" y="2" width="10" height="8" rx="1" fill="#fff"/><rect x="3" y="3.5" width="6" height="4" fill="#2746c8"/></svg>
        Fax 555 010 2469
      </div>
      <div class="contact__item">
        <svg viewBox="0 0 12 12"><circle cx="6" cy="6" r="5" fill="none" stroke="#fff" stroke-width="1.2"/><path d="M1 6 H11 M6 1 C3.5 3.5 3.5 8.5 6 11 M6 1 C8.5 3.5 8.5 8.5 6 11" fill="none" stroke="#fff" stroke-width="1"/></svg>
        www.darekolundmd.example
      </div>
    </div>
  </div>
</section>

</body>
</html>
```